Web site for cutting edge executive coaching and consulting firm | ||
Bravonte | ||
Consulting | ||
Services that increase Performance: - Coaching: Executives, Groups / Teams - Problem Solving - Organizational Change. Focus on: - Holistic approach - Verdessan spirit (colors) - Psychological driven models - Relationship building - sustained outcomes |
I like colors, yet, colors shall not hinder clear reading of text. I like a clear & simple structure of Website. I like to use symbols and/or forms. |
Cutting-Edge Unique/Creative Clean/Simple Professional Exciting Industrial Colorful Elegant Progressive Service Oriented Traditional |
blue | ||
Arial Verdana |

```html
<!DOCTYPE html>
<html lang="en">
<head>
<meta charset="utf-8">
<title>Bravonte – Executive Coaching and Consulting</title>
<link href="https://fonts.googleapis.com/css2?family=Arimo:wght@400;700&display=swap" rel="stylesheet">
<style>
:root{
  --bg-deep:#0a2a78;
  --bg-mid:#1a4fb4;
  --white:#ffffff;
  --brand-blue:#1d4f9c;
  --accent-red:#d8262b;
  --nav-text:#4a6a9a;
  --nav-active:#f08a1a;
  --title-cyan:#2aa7dc;
  --body-grey:#9a9a9a;
  --button-blue:#4f8fcf;
  --band-grey:#dcdcdc;
  --panel-orange-top:#f39a1e;
  --panel-orange-bottom:#fde33b;
  --panel-text:#b0420c;
  --heading-blue:#2e5f95;
  --footer-text:#dfe8ff;
}
*{margin:0;padding:0;box-sizing:border-box}
html,body{width:1200px;height:961px;overflow:hidden}
body{
  font-family:"Arimo",Arial,sans-serif;
  background:radial-gradient(ellipse at 50% 40%,var(--bg-mid) 0%,var(--bg-deep) 75%);
  position:relative;
}
.header{
  position:absolute;left:177px;top:117px;width:844px;height:130px;
  background:linear-gradient(180deg,#ffffff 0%,#eef0f3 100%);
  border-radius:10px;
}
.brand{position:absolute;left:20px;top:38px}
.brand-name{font-size:44px;font-weight:700;color:var(--brand-blue);letter-spacing:1px}
.brand-sub{font-size:11px;color:var(--accent-red);letter-spacing:2px;margin-top:2px;padding-left:4px;text-transform:uppercase}
.tagline{
  position:absolute;right:20px;top:94px;font-size:15px;color:var(--accent-red);
}
.tagline-rule{position:absolute;left:250px;right:20px;top:114px;height:1px;background:var(--accent-red)}
.main{
  position:absolute;left:177px;top:260px;width:844px;height:519px;
  background:var(--white);border-radius:8px;overflow:hidden;
}
.nav{position:absolute;left:20px;top:18px;display:flex;font-size:14px}
.nav a{color:var(--nav-text);text-decoration:none;padding:0 16px;border-right:1px solid #c5cfdd;line-height:16px}
.nav a:last-child{border-right:none}
.nav a.active{color:var(--nav-active)}
.nav-rule{position:absolute;left:20px;right:20px;top:44px;height:1px;background:#c9d3e0}
.nav-active-rule{position:absolute;left:22px;width:68px;top:42px;height:3px;background:var(--nav-active)}
.feature-photo{position:absolute;left:20px;top:62px;width:167px;height:169px;background:linear-gradient(135deg,#c9d2dc,#5f6f84)}
.feature{position:absolute;left:205px;top:62px;width:340px}
.feature h1{font-size:20px;color:var(--title-cyan);font-weight:700;margin-bottom:8px}
.lorem{font-size:12.5px;line-height:15px;color:var(--body-grey);text-align:justify}
.more{
  position:absolute;display:block;width:62px;height:17px;border-radius:3px;
  background:linear-gradient(180deg,#7fb4e6,var(--button-blue));
  color:#fff;font-size:11px;font-weight:700;text-align:center;line-height:17px;
}
.services-panel{
  position:absolute;left:579px;top:62px;width:244px;height:169px;border-radius:4px;
  background:linear-gradient(180deg,var(--panel-orange-top),var(--panel-orange-bottom));
  padding:22px 16px;
}
.services-panel li{list-style:none;display:flex;align-items:center;font-size:14px;font-weight:700;color:var(--panel-text);height:40px}
.services-panel svg{margin-right:10px}
.band{position:absolute;left:0;top:267px;width:844px;height:213px;background:linear-gradient(180deg,var(--band-grey),#f2f2f2)}
.topic{position:absolute;top:39px;width:260px}
.topic h2{font-size:15px;font-weight:700;color:var(--heading-blue);display:flex;align-items:center;margin-bottom:14px}
.topic h2 svg{margin-right:12px}
.video{position:absolute;left:579px;top:18px;width:244px;height:172px;border:2px solid #b7b7b7;border-radius:5px;background:#efefef;padding:6px}
.video-still{width:100%;height:100%;border-radius:3px;background:linear-gradient(180deg,#e8e1d8,#8a8f98);position:relative}
.video-still svg{position:absolute;left:50%;top:50%;transform:translate(-50%,-50%)}
.footer-copy{position:absolute;left:197px;top:794px;font-size:12px;color:var(--footer-text)}
.social{position:absolute;top:786px;display:block;width:30px;height:30px;border-radius:3px}
</style>
</head>
<body>
<header class="header">
  <div class="brand">
    <div class="brand-name">Bravonte</div>
    <div class="brand-sub">Verdessan Consulting</div>
  </div>
  <div class="tagline">Cutting edge executive coaching and consulting</div>
  <div class="tagline-rule"></div>
</header>

<main class="main">
  <nav class="nav">
    <a class="active" href="#">Home</a><a href="#">About Us</a><a href="#">Services</a><a href="#">News</a><a href="#">Contact Us</a><a href="#">Members</a>
  </nav>
  <div class="nav-rule"></div>
  <div class="nav-active-rule"></div>

  <div class="feature-photo" role="img" aria-label="Executive in a suit holding a puzzle piece"></div>
  <section class="feature">
    <h1>Services that increase performance</h1>
    <p class="lorem">Lorem ipsum dolor sit amet, consectetur adipiscing elit. Nunc imperdiet volutpat auctor. Suspendisse sodales rutrum ornare. Quisque ut risus magna, in sollicitudin nibh. Praesent id diam eu lacus vehicula interdum nec non elit. Nullam at sapien vel. Nam blandit metus. Nulla facilisi Lorem ipsum dolor sit amet.</p>
  </section>
  <a class="more" href="#" style="left:475px;top:215px">More ›</a>

  <ul class="services-panel">
    <li><svg width="20" height="20"><circle cx="10" cy="10" r="9" fill="#6b5a12"/></svg>Group Training</li>
    <li><svg width="20" height="20"><circle cx="10" cy="10" r="9" fill="#6b5a12"/><text x="10" y="15" font-size="13" font-weight="700" fill="#fde33b" text-anchor="middle" font-family="Arimo, sans-serif">?</text></svg>Problem Solving</li>
    <li><svg width="20" height="20"><path d="M6 3h8v8h4l-8 7-8-7h4z" fill="#6b5a12"/></svg>Executive Grooming</li>
  </ul>

  <section class="band">
    <div class="topic" style="left:23px">
      <h2><svg width="34" height="30"><rect x="2" y="14" width="8" height="14" fill="#8a8a8a"/><rect x="12" y="8" width="8" height="20" fill="#f0a030"/><rect x="22" y="2" width="8" height="26" fill="#4f8fcf"/></svg>Organisational Change</h2>
      <p class="lorem">Lorem ipsum dolor sit amet, consectetur adipiscing elit. Nunc imperdiet volutpat auctor. Suspendisse sodales rutrum ornare. Quisque ut risus magna, in sollicitudin nibh. Praesent id diam.</p>
    </div>
    <a class="more" href="#" style="left:194px;top:162px">More ›</a>

    <div class="topic" style="left:306px">
      <h2><svg width="34" height="30"><rect x="4" y="10" width="26" height="10" rx="5" fill="#4f8fcf" transform="rotate(-30 17 15)"/></svg>Relationship Building</h2>
      <p class="lorem">Lorem ipsum dolor sit amet, consectetur adipiscing elit. Nunc imperdiet volutpat auctor. Suspendisse sodales rutrum ornare. Quisque ut risus magna, in sollicitudin nibh. Praesent id diam.</p>
    </div>
    <a class="more" href="#" style="left:475px;top:162px">More ›</a>

    <div class="video">
      <div class="video-still" role="img" aria-label="Video still of a smiling business team">
        <svg width="44" height="44"><circle cx="22" cy="22" r="20" fill="#222" stroke="#fff" stroke-width="3"/><path d="M17 13l13 9-13 9z" fill="#fff"/></svg>
      </div>
    </div>
  </section>
</main>

<footer>
  <p class="footer-copy">Copyright © 2011 Bravonte. All Rights Reserved.</p>
  <a class="social" href="#" aria-label="Social profile" style="left:880px;background:#3b5b98"></a>
  <a class="social" href="#" aria-label="Social profile" style="left:925px;background:#b8332a"></a>
  <a class="social" href="#" aria-label="Social profile" style="left:971px;background:#3aa5dd"></a>
</footer>
</body>
</html>
```